Commercial construction contractor website.

We need a website that contains About Us, Contact info, Services, Project pictures and Industry News section

Target Market(s)

I'm building industral/flex spaces/commercial.

Industry/Entity Type

Commercial/industrial construction

Coding

Coded - Design and coding required

Number of Pages Required

5+ page

Font styles to use
Other font styles liked:
• The logo font is Microgramma Pro

Requirements
Must have
• Must have correct company name spelling: Halden Ridge Construction
Nice to have
• I do like to see our logo design implemented in the design
Should not have
• Please do not show big city pictures and business suit people. We are a commercial construction company

```html
<!DOCTYPE html>
<html lang="en">
<head>
<meta charset="utf-8">
<title>Halden Ridge Construction</title>
<link href="https://fonts.googleapis.com/css2?family=Michroma&family=Lato:wght@400;700&family=Montserrat:wght@500;600;700&display=swap" rel="stylesheet">
<style>
:root{
  --blue:#0b6fc2;
  --blue-dark:#0a4f9c;
  --blue-light:#129be0;
  --ink:#2b2b2b;
  --text:#444;
  --grey:#8c8c8c;
  --line:#cfd6de;
  --footer:#1b1c21;
  --white:#fff;
}
*{box-sizing:border-box;margin:0;padding:0}
html,body{width:1200px;height:4264px;overflow:hidden}
body{position:relative;background:var(--white);font-family:'Lato',sans-serif;color:var(--text)}
.abs{position:absolute}
.display{font-family:'Michroma',sans-serif;text-transform:uppercase;letter-spacing:1px}
.btn{position:absolute;display:flex;align-items:center;justify-content:center;gap:6px;font-family:'Montserrat',sans-serif;font-weight:700;font-size:12px;letter-spacing:.5px;text-transform:uppercase}
.btn-solid{background:var(--blue);color:var(--white)}
.btn-outline{border:1.5px solid var(--blue);color:var(--blue);background:var(--white)}
.wordmark{font-family:'Michroma',sans-serif;text-transform:uppercase;color:var(--blue);text-align:center;line-height:1.3}

/* header */
.site-header{left:0;top:0;width:1200px;height:88px;background:var(--white);border-bottom:1px solid #e3e3e3;z-index:3}
.header-logo{left:150px;top:22px;width:140px;font-size:11px}
.topbar{left:710px;top:0;width:490px;height:42px}
.call{left:782px;top:5px;color:var(--white);font-size:11px;line-height:15px}
.call b{font-size:13px;font-family:'Montserrat',sans-serif}
.social{display:flex;gap:8px}
.social span{width:27px;height:27px;border:1.5px solid var(--white);border-radius:50%;display:block}
.nav{left:460px;top:56px;display:flex;gap:0;font-family:'Montserrat',sans-serif;font-size:12px;font-weight:600;color:#333}
.nav a{display:block;padding:0 17px;position:relative;text-decoration:none;color:inherit}
.nav a.active{color:var(--blue)}
.nav a.active::after{content:"";position:absolute;left:17px;right:17px;top:26px;height:3px;background:var(--blue)}

/* hero */
.hero-photo{left:0;top:88px;width:1200px;height:610px;background:linear-gradient(180deg,#55504a 0%,#8a7558 45%,#b08a5a 70%,#6b5a48 100%)}
.hero-shade{left:0;top:88px;width:1200px;height:610px;background:rgba(20,20,30,.35)}
.hero-title{left:0;width:1200px;text-align:center;color:var(--white)}
.hero-arrow{top:368px;width:40px;height:20px}

/* about */
.about-photo{left:160px;top:720px;width:408px;height:356px;clip-path:polygon(25% 0,75% 0,100% 50%,75% 100%,25% 100%,0 50%);background:linear-gradient(135deg,#9fc3e0,#8a7a62 55%,#5a5046)}
.eyebrow{left:608px;top:728px;display:flex;align-items:center;gap:14px;color:var(--grey);font-size:14px}
.eyebrow i{display:block;width:170px;height:1px;background:var(--line)}
.about-title{left:608px;top:758px;font-size:33px;line-height:43px;color:var(--ink)}
.about-title .blue{color:var(--blue)}
.about-copy{left:608px;top:848px;width:440px;font-size:14.5px;line-height:26.5px;color:#333}

/* services */
.services-title{left:0;width:1200px;top:1232px;text-align:center;color:var(--white);font-size:33px}
.svc{color:var(--white);width:230px}
.svc h3{font-family:'Michroma',sans-serif;font-weight:400;font-size:17px;line-height:24px;text-transform:uppercase}
.svc p{font-size:14px;line-height:21px;margin-top:8px;padding-left:2px}

/* gallery */
.sec-title{left:0;width:1200px;text-align:center;font-size:35px;color:var(--blue)}
.sec-title .dark{color:var(--ink)}
.sec-sub{left:0;width:1200px;text-align:center;font-size:14px;line-height:23px;color:#333}
.photo{position:absolute}

/* contact */
.contact-band{left:0;top:2596px;width:1200px;height:617px;background:linear-gradient(135deg,#0d62b3,#0b5aa8 50%,#0a66bd)}
.contact-title{left:158px;top:2662px;color:var(--white);font-size:33px;line-height:43px}
.contact-copy{left:158px;top:2752px;width:420px;color:var(--white);font-size:14px;line-height:23px;font-weight:700}
.c-icon{width:64px;height:64px;border-radius:50%;border:4px solid rgba(255,255,255,.35);background:var(--white);display:flex;align-items:center;justify-content:center}
.c-dot{width:8px;height:8px;border-radius:50%;background:var(--white)}
.c-label{color:var(--white)}
.c-label h4{font-family:'Michroma',sans-serif;font-weight:400;font-size:15px}
.c-label p{font-size:13.5px;line-height:20px;margin-top:6px}
.inquiry{left:608px;top:2668px;width:432px;height:462px;background:var(--white);border-radius:6px;box-shadow:0 10px 0 -2px rgba(255,255,255,.35)}
.field{position:absolute;height:30px;border-bottom:1px solid #9aa5b1;font-size:13px;color:#555;display:flex;align-items:center;gap:8px}

/* news */
.news-card{position:absolute;width:282px}
.news-img{width:282px;height:187px;position:relative}
.news-date{position:absolute;right:0;bottom:0;background:var(--blue);color:var(--white);font-size:12.5px;font-weight:700;padding:6px 12px 6px 14px;display:flex;gap:6px;align-items:center}
.news-card h3{font-family:'Michroma',sans-serif;font-weight:400;font-size:15.5px;line-height:23px;color:#333;margin-top:18px}
.news-card p{font-size:13.5px;line-height:24px;color:#333;margin-top:16px}

/* footer */
.footer-band{left:0;top:3843px;width:1200px;height:421px}
.f-col h4{font-family:'Michroma',sans-serif;font-weight:400;font-size:15px;color:var(--white)}
.f-col h4::after{content:"";display:block;width:30px;height:2px;background:var(--blue-light);margin-top:8px}
.f-col ul{list-style:none;margin-top:14px}
.f-col li{color:#b8bcc4;font-size:13px;line-height:27px}
.f-col p{color:#b8bcc4;font-size:13px;line-height:24px}
.f-contact{display:flex;gap:12px;margin-top:14px}
.copyright{left:0;width:1200px;top:4218px;text-align:center;color:#a9adb5;font-size:13px}
</style>
</head>
<body>

<!-- header -->
<header class="abs site-header">
  <div class="abs wordmark header-logo">Halden Ridge<br>Construction</div>
  <svg class="abs topbar" viewBox="0 0 490 42"><polygon points="18,0 490,0 490,42 0,42" fill="#0b6fc2"/></svg>
  <svg class="abs" style="left:740px;top:10px" width="22" height="22" viewBox="0 0 24 24" fill="none" stroke="#fff" stroke-width="1.6"><path d="M5 3h4l2 5-2.5 1.5a11 11 0 0 0 6 6L16 13l5 2v4a2 2 0 0 1-2 2A17 17 0 0 1 3 5a2 2 0 0 1 2-2z"/></svg>
  <div class="abs call">Call Us:<br><b>555-018-2046</b></div>
  <div class="abs social" style="left:897px;top:7px"><span></span><span></span><span></span><span></span></div>
  <nav class="abs nav">
    <a class="active">HOME</a><a>ABOUT US</a><a>SERVICES</a><a>PROJECT GALLERY</a><a>NEWS</a><a>CONTACT US</a>
  </nav>
</header>

<!-- hero -->
<section>
  <div class="abs hero-photo" role="img" aria-label="Two site engineers in hard hats overlooking a building site under construction"></div>
  <div class="abs hero-shade"></div>
  <svg class="abs" style="left:0;top:590px" width="1200" height="110" viewBox="0 0 1200 110"><polygon points="0,100 600,8 1200,100 1200,110 0,110" fill="#8f8f93"/><polygon points="0,106 600,14 1200,106 1200,110 0,110" fill="#fff"/></svg>
  <div class="abs hero-title display" style="top:328px;font-size:52px;letter-spacing:2px">Halden Ridge</div>
  <div class="abs hero-title" style="top:390px;display:flex;justify-content:center;align-items:center;gap:18px">
    <i style="display:block;width:50px;height:2px;background:#fff"></i>
    <span class="display" style="font-size:38px">Construction</span>
    <i style="display:block;width:50px;height:2px;background:#fff"></i>
  </div>
  <div class="btn btn-solid" style="left:531px;top:455px;width:138px;height:36px">Contact Us <span>&#8594;</span></div>
  <svg class="abs hero-arrow" style="left:91px" viewBox="0 0 40 20" fill="none" stroke="#fff" stroke-width="2"><path d="M40 10H2M10 2 2 10l8 8"/></svg>
  <svg class="abs hero-arrow" style="left:1069px" viewBox="0 0 40 20" fill="none" stroke="#fff" stroke-width="2"><path d="M0 10h38M30 2l8 8-8 8"/></svg>
  <div class="abs" style="left:560px;top:551px;display:flex;gap:6px"><i style="display:block;width:22px;height:3px;background:#fff"></i><i style="display:block;width:22px;height:3px;background:rgba(255,255,255,.5)"></i><i style="display:block;width:22px;height:3px;background:rgba(255,255,255,.5)"></i></div>
</section>

<!-- about -->
<section>
  <div class="abs about-photo" role="img" aria-label="Tower crane and workers at a construction site, framed in a hexagon"></div>
  <div class="abs eyebrow"><i></i>WELCOME TO THE</div>
  <h2 class="abs about-title display" style="font-weight:400"><span class="blue">Halden Ridge</span><br>Construction</h2>
  <p class="abs about-copy">Irure dolor in reprehenderit in voluptate velit esse cillum dolorei eu fugiat nulla pariatur. Excepteur sint occaecat cupidatat nonom proidento sunt in culpa qui officia deserunt mollit anim id estedei laborum. Sed ut perspiciatis unde omnis iste natus error sit doet voluptatem accusantium doloremque laudantium,magnam umo aliquam quaerat voluptatem. Sed ut perspiciatis undem.</p>
  <div class="btn btn-outline" style="left:609px;top:1030px;width:160px;height:40px">More About Us <span>&#8594;</span></div>
</section>

<!-- services -->
<section>
  <svg class="abs" style="left:0;top:1138px" width="1200" height="680" viewBox="0 0 1200 680">
    <defs><linearGradient id="svcGrad" x1="0" y1="0" x2="0" y2="1"><stop offset="0" stop-color="#129be0"/><stop offset="1" stop-color="#0a57ad"/></linearGradient></defs>
    <polygon points="0,112 372,0 1200,0 1200,80 0,80" fill="#9a9a9e"/>
    <polygon points="0,122 372,18 1200,18 1200,602 990,677 0,602" fill="url(#svcGrad)"/>
  </svg>
  <h2 class="abs services-title display" style="font-weight:400">Our Services</h2>
  <svg class="abs" style="left:330px;top:1300px" width="540" height="380" viewBox="0 0 540 380" fill="none">
    <circle cx="270" cy="190" r="182" stroke="rgba(255,255,255,.25)" stroke-width="1.5"/>
    <circle cx="270" cy="190" r="140" fill="rgba(255,255,255,.08)"/>
    <circle cx="270" cy="190" r="118" fill="rgba(255,255,255,.12)"/>
    <g stroke="rgba(255,255,255,.7)" stroke-dasharray="2 3"><path d="M54 62h54M432 62h54M4 190h50M486 190h50M54 330h54M432 330h54"/></g>
  </svg>
  <div class="abs" style="left:505px;top:1395px;width:190px;height:190px;border-radius:50%;background:#fff;box-shadow:0 6px 18px rgba(0,0,0,.25);display:flex;align-items:center;justify-content:center">
    <div class="wordmark" style="font-size:11px">Halden Ridge<br>Construction</div>
  </div>
  <!-- icon circles -->
  <svg class="abs" style="left:436px;top:1325px" width="72" height="72" viewBox="0 0 72 72"><circle cx="36" cy="36" r="34" fill="#fff"/><g fill="none" stroke="#0b6fc2" stroke-width="2"><path d="M22 52V30h10v22M34 52V22h12v30M20 52h32M38 28h4M38 34h4M38 40h4"/></g></svg>
  <svg class="abs" style="left:691px;top:1325px" width="72" height="72" viewBox="0 0 72 72"><circle cx="36" cy="36" r="34" fill="#fff"/><g fill="none" stroke="#0b6fc2" stroke-width="2"><rect x="20" y="20" width="32" height="32"/><path d="M20 31h32M20 41h32M31 20v32M41 20v32"/></g></svg>
  <svg class="abs" style="left:379px;top:1455px" width="72" height="72" viewBox="0 0 72 72"><circle cx="36" cy="36" r="34" fill="#fff"/><g fill="none" stroke="#0b6fc2" stroke-width="2"><path d="M18 44l10-16h26L44 44zM24 44l10-16M32 44l10-16M40 44l10-16"/></g></svg>
  <svg class="abs" style="left:749px;top:1455px" width="72" height="72" viewBox="0 0 72 72"><circle cx="36" cy="36" r="34" fill="#fff"/><g fill="none" stroke="#0b6fc2" stroke-width="2"><rect x="20" y="24" width="30" height="26"/><path d="M26 44l10-10 8 8M44 22l8-6 3 4-8 6z"/></g></svg>
  <svg class="abs" style="left:436px;top:1595px" width="72" height="72" viewBox="0 0 72 72"><circle cx="36" cy="36" r="34" fill="#fff"/><g fill="none" stroke="#0b6fc2" stroke-width="2"><path d="M26 30a10 10 0 0 1 20 0zM24 30h24M29 33a7 7 0 0 0 14 0M22 54v-6a8 8 0 0 1 8-8h12a8 8 0 0 1 8 8v6z"/></g></svg>
  <svg class="abs" style="left:691px;top:1595px" width="72" height="72" viewBox="0 0 72 72"><circle cx="36" cy="36" r="34" fill="#fff"/><g fill="none" stroke="#0b6fc2" stroke-width="2"><path d="M28 54V20M34 54V20M20 20h34M28 26l6-6M28 34l6-6M28 42l6-6M50 20v10M46 30h8v6h-8zM22 54h16"/><rect x="38" y="44" width="16" height="10"/></g></svg>

  <div class="abs svc" style="left:158px;top:1320px"><h3>Commercial<br>Construction</h3><p>Sed ut perspiciatis unde<br>omnis iste natus error..</p></div>
  <div class="abs svc" style="left:158px;top:1457px"><h3>Top Roofing<br>Work</h3><p>Sed ut perspiciatis unde<br>omnis iste natus error..</p></div>
  <div class="abs svc" style="left:158px;top:1589px"><h3>Construction<br>Consultant</h3><p>Sed ut perspiciatis unde<br>omnis iste natus error..</p></div>
  <div class="abs svc" style="left:872px;top:1320px"><h3>Laminate<br>Flooring</h3><p>Sed ut perspiciatis unde<br>omnis iste natus error..</p></div>
  <div class="abs svc" style="left:872px;top:1457px"><h3>Landscape<br>Work</h3><p>Sed ut perspiciatis unde<br>omnis iste natus error..</p></div>
  <div class="abs svc" style="left:872px;top:1589px"><h3>Self-Perform<br>Construction</h3><p>Sed ut perspiciatis unde<br>omnis iste natus error..</p></div>
</section>

<!-- gallery -->
<section>
  <h2 class="abs sec-title display" style="top:1878px;font-weight:400">Project Gallery</h2>
  <p class="abs sec-sub" style="top:1927px">Reprehenderit in voluptate velit esse cillum dolorei eu fugiat<br>nulla pariatur. Excepteur sint occaecat cupidatat</p>
  <div class="photo" style="left:159px;top:2006px;width:375px;height:445px;background:linear-gradient(180deg,#6fa3d4 0%,#b7cde3 45%,#8c8375 70%,#4a4a4c 100%)" role="img" aria-label="Tower cranes over a concrete frame under construction"></div>
  <div class="photo" style="left:541px;top:2006px;width:498px;height:219px;background:linear-gradient(180deg,#2a2a2c,#3b3a38 60%,#1f1f21)" role="img" aria-label="Steel structure silhouette at a construction site"></div>
  <div class="abs" style="left:541px;top:2073px;width:498px;text-align:center;color:#fff">
    <div class="display" style="font-size:19px">Project Name</div>
    <p style="font-size:13.5px;line-height:23px;margin-top:8px">Voluptate velit esse cillum dolorei eu fugiat nulla<br>pariatur. Excepteur sint occaecat cupidatat</p>
  </div>
  <div class="photo" style="left:541px;top:2232px;width:246px;height:219px;background:linear-gradient(160deg,#c8d6e2,#a89a7c 50%,#6e5b3e)" role="img" aria-label="Workers in hard hats on wooden formwork"></div>
  <div class="photo" style="left:793px;top:2232px;width:246px;height:219px;background:linear-gradient(160deg,#2b5fa8,#1d3f7a 55%,#c2452a 85%,#2a3d66)" role="img" aria-label="Welders working with steel in a workshop"></div>
  <div class="btn btn-solid" style="left:485px;top:2487px;width:230px;height:39px">View All Project Gallery <span>&#8594;</span></div>
</section>

<!-- contact -->
<section>
  <div class="abs contact-band" role="img" aria-label="Blue-tinted construction site background"></div>
  <h2 class="abs contact-title display" style="font-weight:400">Contact<br>Information</h2>
  <p class="abs contact-copy">Reprehenderit in voluptate velit esse cillum dolorei eu fugiat nulla pariatur. Excepteur sint occaecat cupidatat</p>
  <svg class="abs" style="left:194px;top:2870px" width="2" height="215"><line x1="1" y1="0" x2="1" y2="215" stroke="rgba(255,255,255,.4)" stroke-dasharray="2 3"/></svg>

  <div class="abs c-icon" style="left:162px;top:2840px"><svg width="26" height="26" viewBox="0 0 24 24" fill="none" stroke="#0b6fc2" stroke-width="1.6"><path d="M12 22s7-7 7-12a7 7 0 0 0-14 0c0 5 7 12 7 12z"/><circle cx="12" cy="10" r="2.5"/></svg></div>
  <div class="abs c-dot" style="left:268px;top:2868px"></div>
  <div class="abs c-label" style="left:290px;top:2834px"><h4>Office Address</h4><p>48 Quarry Lane, Millbrook<br>Vermont</p></div>

  <div class="abs c-icon" style="left:162px;top:2946px"><svg width="24" height="24" viewBox="0 0 24 24" fill="none" stroke="#0b6fc2" stroke-width="1.6"><path d="M5 3h4l2 5-2.5 1.5a11 11 0 0 0 6 6L16 13l5 2v4a2 2 0 0 1-2 2A17 17 0 0 1 3 5a2 2 0 0 1 2-2z"/></svg></div>
  <div class="abs c-dot" style="left:268px;top:2974px"></div>
  <div class="abs c-label" style="left:290px;top:2940px"><h4>Need Help Call Us</h4><p><b>555-018-2046</b></p></div>

  <div class="abs c-icon" style="left:162px;top:3051px"><svg width="26" height="26" viewBox="0 0 24 24" fill="none" stroke="#0b6fc2" stroke-width="1.6"><rect x="3" y="5" width="18" height="14"/><path d="M3 5l9 8 9-8"/></svg></div>
  <div class="abs c-dot" style="left:268px;top:3079px"></div>
  <div class="abs c-label" style="left:290px;top:3045px"><h4>Drop Us Your Mail</h4><p>contact@haldenridge.com</p></div>

  <div class="abs inquiry">
    <h3 class="display" style="font-weight:400;text-align:center;margin-top:36px;font-size:21px;color:#333">Quick Inquiry</h3>
    <p style="text-align:center;font-size:13.5px;line-height:22px;margin-top:10px;color:#444">Duis aute irure dolor in reprehenderit in voluptate<br>velit esse cillum dolore eu fugiat nulla paria.</p>
    <div class="field" style="left:16px;top:140px;width:192px">&#9679; First Name *</div>
    <div class="field" style="left:224px;top:140px;width:192px">&#9679; Last Name *</div>
    <div class="field" style="left:16px;top:202px;width:192px">@ Email Address *</div>
    <div class="field" style="left:224px;top:202px;width:192px">&#9742; Phone No *</div>
    <div class="field" style="left:16px;top:264px;width:400px;height:76px;align-items:flex-start;padding-top:6px">&#9632; Type your message *</div>
    <div class="btn btn-solid" style="left:152px;top:380px;width:130px;height:39px">Send Now <span>&#10148;</span></div>
  </div>
</section>

<!-- news -->
<section>
  <h2 class="abs sec-title display" style="top:3270px;font-weight:400"><span>Latest</span> <span class="dark">News</span></h2>
  <p class="abs sec-sub" style="top:3316px">Reprehenderit in voluptate velit esse cillum dolorei eu<br>fugnulla pariatur. Excepteur sint occaecat</p>

  <article class="news-card" style="left:158px;top:3396px">
    <div class="news-img" role="img" aria-label="Blueprints on a desk with a yellow hard hat" style="background:linear-gradient(135deg,#e9edf1,#cfd6dd 55%,#e7b530 85%)"><span class="news-date">&#9638; 03 Jan, 2022</span></div>
    <h3>Neque Porro Quisquam<br>Est Qui Dolorem</h3>
    <p>Sed do eiusmod tempor incididunt ut do labore et dolore magna aliqua. Ut enim ad minim veniam quis nostrud exercitation.</p>
  </article>
  <article class="news-card" style="left:458px;top:3396px">
    <div class="news-img" role="img" aria-label="Excavator digging on an earthworks site" style="background:linear-gradient(180deg,#d9dbd8,#a38c6d 50%,#5d4a38)"><span class="news-date">&#9638; 03 Jan, 2022</span></div>
    <h3>Neque Porro Quisquam<br>Est Qui Dolorem</h3>
    <p>Sed do eiusmod tempor incididunt ut do labore et dolore magna aliqua. Ut enim ad minim veniam quis nostrud exercitation.</p>
  </article>
  <article class="news-card" style="left:758px;top:3396px">
    <div class="news-img" role="img" aria-label="Worker in orange safety gear laying concrete" style="background:linear-gradient(160deg,#4a3f38,#d36a2e 45%,#5a534e)"><span class="news-date">&#9638; 03 Jan, 2022</span></div>
    <h3>Neque Porro Quisquam<br>Est Qui Dolorem</h3>
    <p>Sed do eiusmod tempor incididunt ut do labore et dolore magna aliqua. Ut enim ad minim veniam quis nostrud exercitation.</p>
  </article>
  <div class="btn btn-outline" style="left:158px;top:3818px;width:130px;height:34px">Read More <span>&#8594;</span></div>
  <div class="btn btn-outline" style="left:458px;top:3818px;width:130px;height:34px">Read More <span>&#8594;</span></div>
  <div class="btn btn-outline" style="left:758px;top:3818px;width:130px;height:34px">Read More <span>&#8594;</span></div>
</section>

<!-- footer -->
<footer>
  <svg class="abs footer-band" viewBox="0 0 1200 421"><polygon points="0,80 312,0 1200,60 1200,421 0,421" fill="#0b6fc2"/><polygon points="0,88 312,10 1200,70 1200,421 0,421" fill="#1b1c21"/></svg>
  <div class="abs wordmark" style="left:150px;top:4040px;width:210px;font-size:14px;color:#1d8ad8">Halden Ridge<br>Construction</div>
  <div class="abs social" style="left:184px;top:4107px;gap:8px"><span></span><span></span><span></span><span></span></div>

  <div class="abs f-col" style="left:423px;top:3955px"><h4>Quick Links</h4><ul><li>Home</li><li>About Us</li><li>Services</li><li>Project Gallery</li><li>News</li><li>Contact Us</li></ul></div>
  <div class="abs f-col" style="left:592px;top:3955px;width:220px"><h4>Contact Us</h4>
    <div class="f-contact"><svg width="14" height="16" viewBox="0 0 24 24" fill="#1d8ad8"><path d="M12 22s7-7 7-12a7 7 0 0 0-14 0c0 5 7 12 7 12z"/></svg><p>48 Quarry Lane, Millbrook<br>Vermont</p></div>
    <div class="f-contact" style="margin-top:6px"><svg width="14" height="16" viewBox="0 0 24 24" fill="#1d8ad8"><path d="M5 3h4l2 5-2.5 1.5a11 11 0 0 0 6 6L16 13l5 2v4a2 2 0 0 1-2 2A17 17 0 0 1 3 5a2 2 0 0 1 2-2z"/></svg><p>Phone:<br>555-018-2046</p></div>
    <div class="f-contact" style="margin-top:6px"><svg width="14" height="16" viewBox="0 0 24 24" fill="#1d8ad8"><rect x="3" y="7" width="18" height="13"/><path d="M3 7l9-4 9 4" fill="#1d8ad8"/></svg><p>Email:<br>contact@haldenridge.com</p></div>
  </div>
  <div class="abs f-col" style="left:833px;top:3955px;width:210px"><h4>Newsletter</h4><p style="margin-top:14px">Subscribe our newsletter to get latest update on your mail</p></div>
  <div class="btn btn-solid" style="left:833px;top:4060px;width:207px;height:39px;background:#1a7ed6">Signup Now <span>&#10148;</span></div>
  <p class="abs copyright">&copy; 2022 Halden Ridge Construction.All right reserved.</p>
</footer>

</body>
</html>
```